Sticker design

We did an instagram post a while back and would like a sticker with the quote on it. https://www.plovanet.com/clip/Kt8Rbw4PzQe/?ref=Y3JmNDhsc2VqcXIxb2Vw

We’d like the quote to be the audio.

We loved the shirts you did last week.

```html
<!DOCTYPE html>
<html lang="en">
<head>
<meta charset="utf-8">
<title>Preflight Buddy Sticker</title>
<link rel="stylesheet" href="https://fonts.googleapis.com/css2?family=Fredoka:wght@600&display=swap">
<style>
  :root {
    --page-bg: #f4f4f3;
    --sticker-white: #ffffff;
    --sticker-edge: #d9d9d9;
    --ink: #111111;
    --wing-blue: #6fc4d8;
    --placeholder: #eef2f3;
    --placeholder-emoji: #e4e4e4;
  }
  html, body {
    margin: 0;
    padding: 0;
    width: 1200px;
    height: 1200px;
    overflow: hidden;
    background: var(--page-bg);
  }
  .sticker-canvas {
    display: block;
    width: 1200px;
    height: 1200px;
  }
  .sticker-edge { fill: var(--sticker-edge); }
  .sticker-body { fill: var(--sticker-white); }
  .wing-stripe { fill: var(--wing-blue); }
  .quote-line {
    font-family: "Fredoka", "Arial Rounded MT Bold", sans-serif;
    font-weight: 600;
    font-size: 62px;
    fill: var(--ink);
  }
  .icon-area { fill: var(--placeholder); }
  .emoji-area { fill: var(--placeholder-emoji); }
</style>
</head>
<body>
<svg class="sticker-canvas" viewBox="0 0 1024 1024" xmlns="http://www.w3.org/2000/svg">
  <g class="sticker-edge">
    <rect x="146" y="266" width="703" height="254" rx="40"/>
    <polygon points="136,521 874,521 700,704 324,704"/>
    <rect x="381" y="516" width="238" height="218" rx="20"/>
  </g>
  <g class="sticker-body">
    <rect x="149" y="269" width="697" height="248" rx="38"/>
    <polygon points="141,524 869,524 698,701 326,701"/>
    <rect x="384" y="519" width="232" height="212" rx="18"/>
  </g>

  <g class="wing wing-left">
    <polygon class="wing-stripe" points="150,533 380,533 380,567 185,567"/>
    <polygon class="wing-stripe" points="205,578 380,578 380,606 235,606"/>
    <polygon class="wing-stripe" points="265,620 380,620 380,646 292,646"/>
    <polygon class="wing-stripe" points="330,660 380,660 380,690 355,690"/>
  </g>
  <g class="wing wing-right">
    <polygon class="wing-stripe" points="632,533 860,533 827,567 632,567"/>
    <polygon class="wing-stripe" points="632,578 807,578 777,606 632,606"/>
    <polygon class="wing-stripe" points="632,620 747,620 720,646 632,646"/>
    <polygon class="wing-stripe" points="632,660 682,660 657,690 632,690"/>
  </g>

  <rect class="icon-area" x="395" y="527" width="212" height="196" rx="10"
        role="img" aria-label="Line icon of a fuel sampler cup with a dripping drop and a small blue airplane"/>

  <text class="quote-line" x="185" y="343" textLength="620" lengthAdjust="spacingAndGlyphs">When your buddy</text>
  <text class="quote-line" x="168" y="418" textLength="665" lengthAdjust="spacingAndGlyphs">asks to help with</text>
  <text class="quote-line" x="168" y="487" textLength="557" lengthAdjust="spacingAndGlyphs">the preflight...</text>

  <circle class="emoji-area" cx="778" cy="468" r="32"
          role="img" aria-label="Smirking emoji"/>
</svg>
</body>
</html>
```